Business Card for Academic Coach

I need a business card designed for me - a private tutor/academic coach.

Glen Mabery
Academic Coach
AB Pellwood University, 1994 Cum Laude
Phone: 404-555-0187
glenrmabery@tutormail-example.com

Subjects
QET and BRT
Math, Physics, Writing

```html
<!DOCTYPE html>
<html lang="en">
<head>
<meta charset="utf-8">
<title>Glen Mabery — Academic Coach Business Card</title>
<link rel="stylesheet" href="https://fonts.googleapis.com/css2?family=Josefin+Sans:wght@300;400&display=swap">
<style>
  :root {
    --backdrop: #d9d9d9;
    --card-black: #0c0c0c;
    --card-black-soft: #1c1c1c;
    --lime: #a6cd3a;
    --lime-light: #c8e04a;
    --green-deep: #6fbf3a;
    --white: #ffffff;
    --white-faint: rgba(255, 255, 255, 0.32);
  }
  * { box-sizing: border-box; margin: 0; padding: 0; }
  html, body {
    width: 900px;
    height: 1200px;
    overflow: hidden;
    background: var(--backdrop);
    font-family: "Josefin Sans", "Helvetica Neue", Arial, sans-serif;
    font-weight: 300;
  }
  .canvas {
    position: relative;
    width: 900px;
    height: 1200px;
    display: flex;
    justify-content: center;
    align-items: center;
    gap: 50px;
  }
  .card {
    position: relative;
    width: 380px;
    height: 665px;
    overflow: hidden;
    box-shadow: 0 10px 30px rgba(0, 0, 0, 0.25);
  }

  /* Front */
  .card--front {
    background: linear-gradient(180deg, var(--card-black) 0%, var(--card-black-soft) 100%);
    color: var(--white);
    text-align: center;
  }
  .front__mark {
    position: absolute;
    top: 215px;
    left: 0;
    right: 0;
    font-size: 44px;
    font-weight: 400;
    color: var(--lime);
    letter-spacing: 1px;
  }
  .front__name {
    position: absolute;
    top: 320px;
    left: 0;
    right: 0;
    font-size: 37px;
    letter-spacing: 1px;
    text-transform: uppercase;
  }
  .front__name .initial { color: var(--lime); }
  .front__title {
    position: absolute;
    top: 378px;
    left: 0;
    right: 0;
    font-size: 17px;
    letter-spacing: 3px;
    text-transform: uppercase;
  }
  .front__wave {
    position: absolute;
    left: 0;
    bottom: 0;
    width: 380px;
    height: 110px;
  }

  /* Back */
  .card--back {
    background: radial-gradient(ellipse at 70% 20%, var(--lime-light) 0%, var(--lime) 40%, var(--green-deep) 100%);
    color: var(--white);
    padding: 0 28px;
  }
  .back__mark {
    position: absolute;
    top: 70px;
    left: 28px;
    font-size: 86px;
    line-height: 1;
    font-weight: 400;
    color: var(--white-faint);
  }
  .back__name {
    position: absolute;
    top: 340px;
    left: 28px;
    font-size: 36px;
    letter-spacing: 1px;
    text-transform: uppercase;
  }
  .back__details {
    position: absolute;
    top: 400px;
    left: 28px;
    right: 20px;
    list-style: none;
    font-size: 16px;
    line-height: 1.65;
    letter-spacing: 0.5px;
  }
  .back__details .phone-icon {
    width: 15px;
    height: 15px;
    vertical-align: -2px;
    margin-right: 6px;
  }
  .back__subjects {
    position: absolute;
    left: 28px;
    bottom: 48px;
    font-size: 16px;
    line-height: 1.65;
    letter-spacing: 0.5px;
  }
</style>
</head>
<body>
<main class="canvas">
  <section class="card card--front" aria-label="Business card front">
    <div class="front__mark">Glen Mabery</div>
    <h1 class="front__name"><span class="initial">G</span>len <span class="initial">M</span>abery</h1>
    <p class="front__title">Academic Coach</p>
    <svg class="front__wave" viewBox="0 0 380 110" preserveAspectRatio="none" aria-hidden="true">
      <path d="M0 60 C60 30 110 45 170 55 C240 68 300 20 380 35 L380 110 L0 110 Z" fill="#222"/>
    </svg>
  </section>

  <section class="card card--back" aria-label="Business card back">
    <div class="back__mark">Glen<br>Mabery</div>
    <h2 class="back__name">Glen Mabery</h2>
    <ul class="back__details">
      <li>
        <svg class="phone-icon" viewBox="0 0 24 24" aria-hidden="true">
          <path fill="#fff" d="M6.6 10.8a15.1 15.1 0 0 0 6.6 6.6l2.2-2.2a1 1 0 0 1 1-.25 11.4 11.4 0 0 0 3.6.57 1 1 0 0 1 1 1V20a1 1 0 0 1-1 1A17 17 0 0 1 3 4a1 1 0 0 1 1-1h3.5a1 1 0 0 1 1 1c0 1.25.2 2.45.57 3.6a1 1 0 0 1-.25 1Z"/>
        </svg>Phone: 404-555-0187
      </li>
      <li>glenrmabery@tutormail-example.com</li>
      <li>AB Pellwood University,</li>
      <li>1994 Cum Laude</li>
    </ul>
    <div class="back__subjects">
      <p>QET and BRT</p>
      <p>Math, Physics, Writing</p>
    </div>
  </section>
</main>
</body>
</html>
```